Online Marketing Agency Website

We are an online marketing agency that specializes in search marketing (SEM) for businesses of all sizes. Our core services include local search marketing, seo, paid search, paid social, graphic design, video production/editing and website design. We have an existing website that we launched a number of years ago but it's very outdated and we're currently too busy to design a new version.

Target Market(s)

Any business that needs online marketing services with an emphasis on search marketing.

Industry/Entity Type

Ad Agency

Number of Pages Required

4 page

Font styles to use
Sans Serif

Requirements
Must have
• Home page, interior page, blog page, contact us page.
Look and feel should be modern and clean and easy to navigate.
Sections for call outs for specific services: Business Marketing Strategy, Content Creation and Marketing, Graphic & Publication Design, Pay Per Click (PPC) Management, Search Engine Optimization, Social Media Management, Video Production & Editing, Website Hosting & Management, Website Design & Development
Use color from logo that was uploaded.

```html
<!DOCTYPE html>
<html lang="en">
<head>
<meta charset="utf-8">
<title>Ascend Digital — Online Marketing Agency</title>
<link href="https://fonts.googleapis.com/css2?family=Poppins:wght@300;400;500;600;700;800&display=swap" rel="stylesheet">
<style>
:root{
  --orange:#f4511e;
  --orange-light:#ff7a3d;
  --ink:#1f1f1f;
  --muted:#6b6b6b;
  --line:#e6e6e6;
  --dark:#2e2e2e;
  --grey-wave:#cfcfcf;
  --white:#ffffff;
}
*{margin:0;padding:0;box-sizing:border-box}
html,body{width:1200px;height:3734px;overflow:hidden;background:var(--white)}
body{font-family:'Poppins',sans-serif;color:var(--ink)}
.page{position:relative;width:1200px;height:3734px;overflow:hidden}
.abs{position:absolute}
/* header */
.brand{left:184px;top:10px;display:flex;align-items:center;gap:8px}
.brand-dot{width:22px;height:22px;border-radius:50%;background:var(--orange)}
.brand-name{font-size:13px;font-weight:700;color:var(--ink);letter-spacing:.3px;line-height:1.1}
.brand-tag{font-size:8px;color:var(--muted)}
.nav{left:536px;top:30px;display:flex;gap:16px;font-size:13px;font-weight:500;text-transform:uppercase}
.nav .active{color:var(--orange)}
.nav-mark{left:553px;top:0;width:2px;height:24px;background:var(--orange)}
.btn{display:flex;align-items:center;justify-content:center;border-radius:22px;background:linear-gradient(90deg,var(--orange),var(--orange-light));color:var(--white);font-weight:600;text-transform:uppercase;box-shadow:0 6px 14px rgba(244,81,30,.3)}
.btn-contact{left:888px;top:19px;width:126px;height:39px;font-size:10px}
/* hero */
.hero{left:0;top:78px;width:1200px;height:560px;background:linear-gradient(120deg,#3a3a3a,#1e1e1e 55%,#2b2b2b)}
.hero-title{left:191px;top:205px;color:var(--white);font-size:33px;line-height:38px;text-transform:uppercase;font-weight:400}
.hero-title b{font-weight:800}
.hero-social{left:191px;top:330px;display:flex;gap:18px;color:var(--white);font-size:11px;font-weight:600}
.btn-quote{left:190px;top:370px;width:124px;height:40px;font-size:10px}
.play-ring{left:725px;top:228px;width:130px;height:130px;border-radius:50%;background:rgba(244,81,30,.18)}
.play{left:747px;top:250px;width:86px;height:86px;border-radius:50%;background:var(--orange);display:flex;align-items:center;justify-content:center}
.watch{left:740px;top:377px;width:100px;text-align:center;color:var(--white);font-size:13px;font-weight:500}
.mouse{left:590px;top:508px;width:16px;height:26px;border:2px solid var(--white);border-radius:8px}
.mouse::after{content:"";position:absolute;left:5px;top:5px;width:2px;height:6px;background:var(--white)}
/* section heads */
.kicker{font-size:12px;color:var(--ink)}
.title{font-size:40px;font-weight:800;color:var(--orange);letter-spacing:-1px;line-height:1.15}
.center{left:0;width:1200px;text-align:center}
/* works */
.work{top:797px;height:305px;overflow:hidden}
.work h3{position:absolute;left:30px;top:38px;font-size:28px;font-weight:400}
.work h3 b{font-weight:800}
.work p{position:absolute;left:30px;top:82px;font-size:13px;line-height:24px;text-transform:uppercase}
.work .art{position:absolute}
.arrows{display:flex;gap:18px}
.arrows span{width:12px;height:12px;border-left:2px solid var(--ink);border-bottom:2px solid var(--ink);transform:rotate(45deg);display:block}
.arrows span+span{transform:rotate(-135deg)}
/* services */
.svc{top:1308px;width:235px;height:253px;background:var(--white);box-shadow:0 6px 22px rgba(0,0,0,.1);text-align:center}
.svc svg{margin-top:30px}
.svc h4{font-size:14px;font-weight:600;line-height:18px;margin-top:14px;text-transform:uppercase}
.svc p{font-size:11px;line-height:15px;color:var(--muted);padding:0 18px;margin-top:12px}
.svc .more{font-size:10px;font-weight:600;margin-top:12px;display:block}
.svc .more i{color:var(--orange);font-style:normal}
/* why */
.why-intro{left:184px;top:1724px;width:410px;font-size:12px;line-height:21px;color:var(--muted)}
.feat{left:184px;width:420px}
.feat svg{position:absolute;left:0;top:0}
.feat h5{margin-left:66px;font-size:14px;font-weight:600}
.feat p{margin-left:66px;font-size:11.5px;line-height:21px;color:var(--muted);margin-top:4px}
.photo{background:linear-gradient(135deg,#2b2b2b,#101010 60%,#3a1a14)}
/* testimonial */
.t-card{left:593px;top:2333px;width:417px;height:293px;background:var(--white);box-shadow:0 8px 26px rgba(0,0,0,.1)}
.t-avatar{left:44px;top:17px;width:104px;height:104px;border-radius:50%;border:4px solid #f8b9a2;background:linear-gradient(160deg,#c9d9e8,#8fa9c2)}
.t-text{left:36px;top:136px;width:345px;font-size:12px;line-height:20px;color:var(--muted)}
.t-name{left:36px;top:236px;font-size:12px;font-weight:600}
.t-role{left:36px;top:258px;font-size:10px;color:var(--muted)}
/* blog */
.post{top:2804px;width:264px}
.post .thumb{height:146px}
.post h6{font-size:19px;font-weight:600;line-height:24px;margin-top:22px}
.post time{display:block;font-size:12px;font-weight:600;color:var(--orange);margin-top:14px}
.btn-view{left:885px;top:2731px;width:125px;height:38px;font-size:12px;font-weight:500}
/* clients */
.client{top:3244px;width:170px;text-align:center;font-size:16px;font-weight:600;color:#222;white-space:nowrap}
/* footer */
.foot-col h6{font-size:13px;font-weight:600;color:var(--white)}
.foot-col ul{list-style:none;margin-top:14px}
.foot-col li,.foot-col p{font-size:13.5px;color:var(--white);line-height:24.6px}
.foot-rule{left:184px;top:3678px;width:832px;height:1px;background:rgba(255,255,255,.45)}
.copy{top:3701px;font-size:10px;color:var(--white)}
</style>
</head>
<body>
<div class="page">

  <!-- header -->
  <div class="abs nav-mark"></div>
  <div class="abs brand">
    <span class="brand-dot"></span>
    <div><div class="brand-name">ASCEND DIGITAL</div><div class="brand-tag">Online Marketing. Elevated</div></div>
  </div>
  <nav class="abs nav">
    <span class="active">Home</span><span>Portfolio</span><span>Services ⌄</span><span>About</span><span>Blog</span>
  </nav>
  <a class="abs btn btn-contact">Contact us</a>

  <!-- hero -->
  <div class="abs hero" role="img" aria-label="Black and white photo of a busy agency office with people at desks"></div>
  <svg class="abs" style="left:0;top:500px" width="1200" height="140" viewBox="0 0 1200 140">
    <path d="M0 18 C300 80 700 90 1200 10 L1200 140 L0 140Z" fill="var(--grey-wave)"/>
    <path d="M0 50 C350 120 750 110 1200 30 L1200 140 L0 140Z" fill="var(--white)"/>
  </svg>
  <h1 class="abs hero-title">Ascend Digital is<br><b>a full-service online</b><br>marketing agency</h1>
  <div class="abs hero-social"><span>Facet</span><span>Pixo</span><span>Chirp</span></div>
  <a class="abs btn btn-quote">Request a quote</a>
  <div class="abs play-ring"></div>
  <div class="abs play"><svg width="22" height="22" viewBox="0 0 22 22"><path d="M6 3 L19 11 L6 19Z" fill="none" stroke="#fff" stroke-width="2.5" stroke-linejoin="round"/></svg></div>
  <div class="abs watch">WATCH US</div>
  <div class="abs mouse"></div>

  <!-- recent works -->
  <div class="abs center kicker" style="top:703px">&lt; PORTFOLIO /&gt;</div>
  <h2 class="abs center title" style="top:725px">Recent Works</h2>

  <div class="abs work" style="left:0;width:355px;background:#f6efe2">
    <h3 style="left:-32px">Title <b>01</b></h3>
    <p style="left:-32px">Brand, Graphic Design</p>
    <div class="art" style="left:0;top:120px;width:355px;height:185px;background:linear-gradient(135deg,#f6efe2,#f4b6a6 50%,#f8d27a)" role="img" aria-label="Playful line illustration of characters with fruit"></div>
  </div>
  <div class="abs work" style="left:384px;width:406px;background:#eceef1">
    <h3>Title <b>02</b></h3>
    <p>Brand,<br>App Developement</p>
    <div class="art" style="left:170px;top:0;width:236px;height:305px;background:linear-gradient(150deg,#f4f4f4,#c9cbd0)" role="img" aria-label="Angled mobile app screens mockup"></div>
  </div>
  <div class="abs work" style="left:814px;width:386px;height:310px;background:#f7c4c7">
    <h3>Title <b>03</b></h3>
    <p>Brand, Website<br>Design</p>
    <div class="art" style="left:150px;top:50px;width:236px;height:260px;background:linear-gradient(160deg,#ffffff,#d9e6f5 60%,#f7c4c7)" role="img" aria-label="Fitness website layout with illustrated runner"></div>
  </div>
  <div class="abs arrows" style="left:584px;top:1150px"><span></span><span></span></div>

  <!-- services -->
  <div class="abs kicker" style="left:203px;top:1224px">&lt; WHAT WE DO /&gt;</div>
  <h2 class="abs title" style="left:196px;top:1244px">Our Services</h2>
  <div class="abs arrows" style="left:955px;top:1262px"><span></span><span></span></div>

  <div class="abs svc" style="left:199px">
    <svg width="58" height="52" viewBox="0 0 58 52" fill="none" stroke="#3fa35b" stroke-width="2"><rect x="3" y="6" width="44" height="30" rx="2"/><path d="M20 36v8M14 46h22"/><circle cx="46" cy="10" r="7"/><circle cx="22" cy="21" r="5"/></svg>
    <h4>Business Marketing<br>Strategy</h4>
    <p>Let us strategize the big picture for you. With decades of experience, we have seen what works...</p>
    <span class="more">learn more <i>→</i></span>
  </div>
  <div class="abs svc" style="left:482px">
    <svg width="58" height="52" viewBox="0 0 58 52" fill="none" stroke="#3d7fd1" stroke-width="2"><rect x="6" y="4" width="30" height="40" rx="4"/><rect x="28" y="8" width="22" height="18" rx="2"/><path d="M15 22c3-4 8 0 6 4l-3 3-3-3c-2-2 0-4 0-4z"/><path d="M34 30v14h14"/></svg>
    <h4>Content Creation<br>and Marketing</h4>
    <p>You've heard it before. "Content is king." Searchly loves it and potential customers expect it...</p>
    <span class="more">learn more <i>→</i></span>
  </div>
  <div class="abs svc" style="left:767px">
    <svg width="64" height="52" viewBox="0 0 64 52" fill="none" stroke="#e2333f" stroke-width="2"><rect x="3" y="3" width="58" height="36" rx="2"/><path d="M26 39v7M16 48h32"/><path d="M10 14h6l4 12h14l3-9H18"/><path d="M42 13h12M42 19h12M42 25h12"/></svg>
    <h4>Graphic &amp; Publication<br>Design</h4>
    <p>Our designers have decades of experience in everything from tradeshow graphics to...</p>
    <span class="more">learn more <i>→</i></span>
  </div>

  <!-- why choose -->
  <div class="abs kicker" style="left:184px;top:1638px">&lt; WHY CHOOSE US /&gt;</div>
  <h2 class="abs title" style="left:184px;top:1666px">Work with Us Today</h2>
  <p class="abs why-intro">We can handle any element of your online marketing so you can get back to doing what you do best — growing your business.</p>

  <div class="abs feat" style="top:1781px">
    <svg width="44" height="54" viewBox="0 0 44 54" fill="none" stroke="#3d7fd1" stroke-width="2"><path d="M10 4h24v14a12 12 0 0 1-24 0z"/><path d="M10 8H3c0 8 4 12 8 12M34 8h7c0 8-4 12-8 12"/><path d="M22 30v10M12 42h20v8H12z"/></svg>
    <h5>Experience our award winning developers</h5>
    <p>We source our developers from all over the world, from<br>winners of global hackathon competitions.</p>
  </div>
  <div class="abs feat" style="top:1874px">
    <svg width="44" height="44" viewBox="0 0 44 44" fill="none" stroke="#3fa35b" stroke-width="2"><rect x="2" y="12" width="40" height="22" rx="2"/><circle cx="22" cy="23" r="6"/><path d="M8 6h28l-4-4M36 40H8l4 4"/></svg>
    <h5>Money back guarantee + warranty</h5>
    <p>We care about you, which is why we offer a money back<br>guarantee and one month warranty with all projects.</p>
  </div>
  <div class="abs feat" style="top:1963px">
    <svg width="44" height="50" viewBox="0 0 44 50" fill="none" stroke="#f4511e" stroke-width="2"><path d="M8 22a14 14 0 0 1 28 0v6"/><rect x="4" y="20" width="7" height="12" rx="2"/><rect x="33" y="20" width="7" height="12" rx="2"/><path d="M6 48c2-10 30-10 32 0"/></svg>
    <h5>Dedicated live support team</h5>
    <p>Our agents are standing by to answer your questions<br>and provide support whenever you need it.</p>
  </div>
  <div class="abs feat" style="top:2053px">
    <svg width="44" height="50" viewBox="0 0 44 50" fill="none" stroke="#e2333f" stroke-width="2"><circle cx="22" cy="20" r="16"/><circle cx="22" cy="20" r="6"/><path d="M16 40h12M18 46h8"/></svg>
    <h5>We use the latest technology</h5>
    <p>Our members are trained to use the latest cutting edge<br>software and equipment that the industry has to offer.</p>
  </div>

  <div class="abs photo" style="left:616px;top:1649px;width:584px;height:481px" role="img" aria-label="Smiling man with arms crossed shown on a laptop screen"></div>

  <!-- testimonials -->
  <div class="abs" style="left:7px;top:2239px;width:565px;height:387px;background:radial-gradient(ellipse at center,#ececec,#f7f7f7 70%,#fff)" role="img" aria-label="Dotted world map with portraits of clients around the globe"></div>
  <div class="abs kicker" style="left:593px;top:2218px">&lt; TESTIMONIALS /&gt;</div>
  <h2 class="abs title" style="left:593px;top:2240px;line-height:46px">See What Our Clients<br>Have to Say</h2>
  <div class="abs t-card">
    <div class="abs t-avatar" role="img" aria-label="Portrait of the client"></div>
    <p class="abs t-text">Lorem Ipsum is simply dummy text of the printing and typesetting industry. Lorem Ipsum has been the industry's standard dummy text ever since the 1500s, when an unknown printer took it to make a type specimen book.</p>
    <div class="abs t-name">Jon Meyer</div>
    <div class="abs t-role">Northgate Co, CEO</div>
    <div class="abs arrows" style="left:352px;top:248px"><span></span><span></span></div>
  </div>

  <!-- blog -->
  <div class="abs kicker" style="left:184px;top:2706px">&lt; BLOGS/&gt;</div>
  <h2 class="abs title" style="left:180px;top:2730px">Recent Articles</h2>
  <a class="abs btn btn-view">View all</a>

  <article class="abs post" style="left:183px">
    <div class="thumb" style="background:linear-gradient(135deg,#e9edf2,#9fb6cf)" role="img" aria-label="Hand holding a tablet showing pay per click graphics"></div>
    <h6>It is a long established fact that a reader will be distracted</h6>
    <time>Feb 11, 2020</time>
  </article>
  <article class="abs post" style="left:468px">
    <div class="thumb" style="background:linear-gradient(135deg,#3a3a3a,#8a8a8a)" role="img" aria-label="Hands typing on a phone with social engagement counters"></div>
    <h6>There are many variations of passages of Lorem Ipsum available</h6>
    <time>Jan 11, 2020</time>
  </article>
  <article class="abs post" style="left:752px">
    <div class="thumb" style="background:linear-gradient(135deg,#f2f2f2,#c4c4c4)" role="img" aria-label="Magnifying glass over an advertising web page"></div>
    <h6>Contrary to popular belief, Lorem Ipsum is not simply random text</h6>
    <time>Dec 29, 2019</time>
  </article>

  <!-- clients -->
  <div class="abs center kicker" style="top:3132px">&lt; CLIENTS /&gt;</div>
  <h2 class="abs center title" style="top:3152px">Our Happy Clients</h2>
  <div class="abs client" style="left:123px">Harbor &amp; Pine</div>
  <div class="abs client" style="left:303px">Solway Group</div>
  <div class="abs client" style="left:497px">Brightmere</div>
  <div class="abs client" style="left:685px">Calder Optics</div>
  <div class="abs client" style="left:882px">Tallis Goods</div>

  <!-- footer -->
  <svg class="abs" style="left:0;top:3300px" width="1200" height="434" viewBox="0 0 1200 434" preserveAspectRatio="none">
    <path d="M0 40 C200 0 380 70 600 40 C820 10 1000 60 1200 20 L1200 434 L0 434Z" fill="#d6d6d6"/>
    <path d="M0 70 C220 30 400 100 620 70 C840 40 1020 90 1200 55 L1200 434 L0 434Z" fill="var(--dark)"/>
    <path d="M0 125 C250 85 430 140 640 110 C860 80 1030 120 1200 95 L1200 434 L0 434Z" fill="var(--orange)"/>
  </svg>

  <div class="abs foot-col" style="left:184px;top:3488px">
    <h6>Quick Links</h6>
    <ul><li>Web Design</li><li>Software/Script Development</li><li>App Development</li><li>Photography/Videography</li><li>Graphic Design</li></ul>
  </div>
  <div class="abs foot-col" style="left:468px;top:3488px">
    <h6>Other Links</h6>
    <ul><li>About Us</li><li>Portfolio</li><li>Services</li><li>Blog</li><li>Contact</li></ul>
  </div>
  <div class="abs foot-col" style="left:651px;top:3488px">
    <h6>Offices</h6>
    <ul><li>1480 Maple Ridge Road, LA,<br>SBT 12345</li><li>&nbsp;</li><li>tel : 555-014-2290</li><li>email : info@ascenddigital.example</li></ul>
  </div>
  <div class="abs foot-col" style="left:917px;top:3488px">
    <h6>Follow Us</h6>
    <ul><li>Facet &nbsp; Pixo &nbsp; Chirp</li></ul>
  </div>
  <div class="abs foot-rule"></div>
  <div class="abs center copy">© 2020 by Ascend Digital. All Rights Reserved. | Privacy Policy | Terms &amp; Conditions</div>

</div>
</body>
</html>
```